BirchLane Hotel
BUSINESS CARDS, LETTERHEAD, ENVELOPES, FAX COVER, EMAIL SIGNATURE, signage, car
BirchLane Hotel - Hospitality Industry
Creative Brief
Simple
DOHYUN KWAK
President & C.E.O
B2 Sora Bldg. 412-5 Mokhwa-dong, Seocho-gu, Seoul, 137-914, Korea
oliver@blhotelgroup.com
www.blhotelgroup.com
BirchLane Pohang: 218-4 Hwajin-dong, Bukgu, Pohang, Korea BirchLane Gunsan: 457 Maeryeong-dong, Gunsan, Korea

```html
<!DOCTYPE html>
<html lang="en">
<head>
<meta charset="utf-8">
<title>BirchLane Hotel – Business Card</title>
<link rel="stylesheet" href="https://fonts.googleapis.com/css2?family=Questrial&display=swap">
<style>
  :root {
    --stage: #e6e8e6;
    --card-green: #17805a;
    --brand-green: #7cbf2c;
    --paper: #ffffff;
    --ink-grey: #8a8a8a;
  }
  html, body {
    margin: 0;
    width: 1200px;
    height: 1104px;
    overflow: hidden;
    background: var(--stage);
    font-family: "Questrial", "Century Gothic", sans-serif;
  }
  .canvas { position: relative; width: 1200px; height: 1104px; }

  .card { position: absolute; box-sizing: border-box; }
  .card-front {
    left: 77px; top: 247px; width: 698px; height: 378px;
    background: var(--card-green);
  }
  .card-back {
    left: 466px; top: 634px; width: 687px; height: 466px;
    background: var(--paper);
    box-shadow: 0 2px 10px rgba(0,0,0,0.12);
  }

  .brand-mark { position: absolute; border-radius: 50%; background: var(--brand-green); }
  .card-front .brand-mark { width: 120px; height: 120px; left: 289px; top: 50px; }
  .card-back .brand-mark { width: 150px; height: 150px; left: 125px; top: 60px; }

  .brand-name { position: absolute; margin: 0; white-space: nowrap; font-weight: 400; text-align: center; }
  .card-front .brand-name {
    left: 0; width: 698px; top: 250px;
    font-size: 46px; color: var(--paper);
  }
  .card-back .brand-name {
    left: 20px; width: 360px; top: 318px;
    font-size: 36px; color: var(--brand-green);
  }

  .contact { position: absolute; left: 380px; top: 78px; width: 290px; color: var(--ink-grey); }
  .contact-name { margin: 0; font-size: 30px; font-weight: 400; color: var(--brand-green); letter-spacing: 1px; }
  .contact-title { margin: 4px 0 0; font-size: 17px; color: var(--ink-grey); }
  .contact-address { margin: 29px 0 0; font-size: 14px; line-height: 20px; font-style: normal; white-space: nowrap; }
  .contact-lines { list-style: none; margin: 17px 0 0; padding: 0; font-size: 14px; line-height: 20px; white-space: nowrap; }
</style>
</head>
<body>
<main class="canvas">
  <section class="card card-front" aria-label="Business card front">
    <span class="brand-mark" aria-hidden="true"></span>
    <h1 class="brand-name">BirchLane Hotel</h1>
  </section>

  <section class="card card-back" aria-label="Business card back">
    <span class="brand-mark" aria-hidden="true"></span>
    <p class="brand-name">BirchLane Hotel</p>

    <div class="contact">
      <h2 class="contact-name">DOHYUN KWAK</h2>
      <p class="contact-title">President &amp; C.E.O</p>
      <address class="contact-address">
        B2 Sora Bldg. 412-5 Mokhwa-<br>dong,<br>
        Seocho-gu, Seoul, 137-914,<br>Korea
      </address>
      <ul class="contact-lines">
        <li>P: 02-531-4820</li>
        <li>F: 02-531-4823</li>
        <li>C: 010-4286-1597</li>
        <li>E: oliver@blhotelgroup.com</li>
        <li>www.blhotelgroup.com</li>
      </ul>
    </div>
  </section>
</main>
</body>
</html>
```